Turfbloom.com needs a professional yet bold design to share our differences and convert customers!

We need web design for the only company to offer same day & next day lawn care services to the North Carolina Piedmont Triad area! Customers will be able to view cost and book their lawn service in 5 minutes via our website. We need to promote the following that set us apart: 1: No Contract 2: Instant Scheduling 3: Same Day Service 4: Fully Licensed and Insured, 5: Money Back Guarantee. We are the ONLY company in the area to offer this service.
The site needs to be bold to show the reasons we are different. "in your face", yet professional enough to earn a customer's trust. Inspiration can be drawn from sites such as tidyfoxcrew.com, however the creative piece will be up to you to create a website that is perhaps unique, slightly tacky, different, etc. The key is for it to be the BEST in the area and easy to use without confusing customers. Must be able to allure customers in and have an easy checkout and booking procedure.
Updates

Target Market(s)

People that want a simple, quick, and easy way to get someone to mow their grass!

Industry/Entity Type

It Company

Logo Text

Turf Bloom logo design opportunity to be offered as well.

Number of Pages Required

1 page

Requirements
Must have
• simple, bold, yet instill trust from the public.
Nice to have
• Need chat now, book now, popups showing % off that day. Need Zip code entry to price lawns. Need it to emphasize the quick process, reliability of the company, etc.

```html
<!DOCTYPE html>
<html lang="en">
<head>
<meta charset="utf-8">
<title>Turf Bloom — Web Design</title>
<link rel="stylesheet" href="https://fonts.googleapis.com/css2?family=Roboto:wght@300;400;500;700&display=swap">
<style>
:root{
  --orange:#e8601c;
  --charcoal:#3b3b3b;
  --ink:#333333;
  --muted:#7a7a7a;
  --light-grey:#e6e6e6;
  --band-grey:#e9e9e9;
  --paper:#ffffff;
  --grass-dark:#1f5a12;
  --grass:#3f9a1e;
  --grass-light:#8fd14a;
  --shadow:rgba(0,0,0,.12);
}
*{margin:0;padding:0;box-sizing:border-box}
html,body{width:1200px;height:900px;overflow:hidden;background:var(--paper)}
body{position:relative;font-family:"Roboto",Arial,sans-serif;color:var(--ink)}

/* brand strip */
.brand-strip{position:absolute;left:0;top:0;height:17px;display:flex}
.brand-strip span{display:block;height:100%}
.strip-light{width:83px;background:var(--light-grey)}
.strip-dark{width:122px;background:var(--charcoal)}
.strip-orange{width:145px;background:var(--orange)}

/* badge logo */
.badge-logo{position:absolute;left:84px;top:160px;width:94px;text-align:left}
.badge-name{font-size:19px;font-weight:500;color:var(--charcoal);line-height:1}
.badge-url{font-size:10px;color:var(--charcoal);margin-top:3px;letter-spacing:.2px}
.badge-shield{display:block;margin-top:4px}

/* wordmark */
.wordmark{position:absolute;left:286px;top:180px;font-size:54px;font-weight:400;color:var(--charcoal);letter-spacing:-.5px;line-height:1}

/* hero screen */
.hero-screen{position:absolute;left:70px;top:330px;width:780px;height:560px;overflow:hidden;border-radius:4px;box-shadow:0 6px 24px var(--shadow)}
.hero-photo{position:absolute;inset:0;background:
  radial-gradient(ellipse at 55% 20%,#6b6a4d 0%,transparent 55%),
  linear-gradient(180deg,#4a4a3a 0%,#3f6b2a 38%,var(--grass) 60%,var(--grass-dark) 100%)}
.hero-nav{position:absolute;top:44px;right:110px;display:flex;gap:30px;color:#fff;font-size:17px;font-weight:300}
.hero-burger{position:absolute;top:44px;right:56px}
.hero-logo{position:absolute;left:58px;top:108px;color:#fff;font-size:30px;font-weight:400}
.hero-offer{position:absolute;left:500px;top:190px;color:#fff}
.hero-percent{font-size:46px;font-weight:300;text-align:right;padding-right:18px}
.hero-tagline{font-size:18px;font-weight:300;line-height:1.45;width:220px}
.hero-book{position:absolute;left:540px;top:300px;width:180px;height:56px;background:var(--orange);color:#fff;font-size:19px;font-weight:300;display:flex;align-items:center;justify-content:center}
.hero-chevron{position:absolute;left:380px;bottom:26px}

/* full page preview */
.page{position:absolute;left:869px;top:32px;width:241px;height:835px;background:var(--paper);box-shadow:0 2px 10px var(--shadow);overflow:hidden;font-size:3.4px;line-height:1.45}
.page section{position:absolute;left:0;width:100%}
.mini-hero{top:0;height:121px}
.mini-hero .photo{position:absolute;inset:0;background:linear-gradient(180deg,#4f5a3c 0%,#4c9a27 55%,#2f7318 100%)}
.mini-logo{position:absolute;left:9px;top:8px;color:#fff;font-size:6px;font-weight:500}
.mini-nav{position:absolute;right:16px;top:8px;display:flex;gap:6px;color:#fff;font-size:3.6px}
.mini-burger{position:absolute;right:9px;top:8px;width:6px;border-top:1px solid #fff;border-bottom:1px solid #fff;height:3px}
.mini-offer{position:absolute;left:175px;top:55px;color:#fff;width:50px}
.mini-offer b{display:block;font-size:9px;font-weight:300;text-align:right}
.mini-book{position:absolute;left:175px;top:72px;width:38px;height:8px;background:var(--orange);color:#fff;font-size:3.4px;display:flex;align-items:center;justify-content:center}
.mini-chevron{position:absolute;left:116px;top:108px}

.section-title{text-align:center;font-size:5px;font-weight:500;color:var(--ink)}
.section-rule{width:32px;height:1px;background:var(--orange);margin:6px auto 6px}
.section-text{width:170px;margin:0 auto;text-align:center;color:var(--muted)}

.we-do{top:137px}
.service-band{top:240px;height:121px;background:var(--band-grey)}
.service-cards{top:197px;height:100px}
.card{position:absolute;background:#fff;box-shadow:0 1px 2px var(--shadow)}
.card .img{width:100%;background:linear-gradient(180deg,var(--grass-light),var(--grass))}
.card .caption{padding:3px 5px;color:var(--muted)}
.card .caption strong{display:block;color:var(--ink);font-weight:500}
.card-1{left:31px;top:10px;width:52px}.card-1 .img{height:62px}
.card-2{left:93px;top:0;width:55px}.card-2 .img{height:73px;background:linear-gradient(180deg,#6fbf3a,#2e8a1a)}
.card-3{left:158px;top:20px;width:52px}.card-3 .img{height:52px}

.zip{top:314px;text-align:center}
.zip-label{font-size:3.4px;font-weight:500;color:var(--ink)}
.zip-form{margin:5px auto 0;width:116px;height:22px;background:#fff;display:flex;align-items:center;gap:4px;padding:0 6px}
.zip-input{width:62px;height:8px;border:.5px solid #999;color:var(--muted);font-size:2.8px;padding-left:2px;display:flex;align-items:center}
.zip-btn{width:37px;height:8px;background:var(--orange);color:#fff;font-size:2.8px;display:flex;align-items:center;justify-content:center}

.why{top:372px}
.features{top:420px;height:80px}
.feature{position:absolute;display:flex;gap:3px;width:70px;color:var(--muted);font-size:2.9px}
.feature strong{display:block;color:var(--ink);font-weight:500}
.feature svg{flex:none}
.f1{left:16px;top:0}.f2{left:88px;top:0}.f3{left:163px;top:0}
.f4{left:52px;top:32px}.f5{left:150px;top:32px}

.we-are{top:497px}
.we-are-badge{display:block;margin:6px auto 0}

.video{top:575px;height:121px}
.video .photo{position:absolute;inset:0;background:linear-gradient(180deg,#5a8a3a 0%,#4b9a26 50%,#2c6a15 100%)}
.video .section-title{position:relative;color:#fff;margin-top:14px}
.video .section-text{position:relative;color:#eaf5e0}
.video .play{position:absolute;left:107px;top:63px}

.contact{top:696px;height:94px;background:var(--band-grey)}
.contact .section-title{margin-top:9px}
.contact-form{position:absolute;left:54px;top:34px;width:134px;height:42px}
.field{position:absolute;background:#fff;color:var(--muted);font-size:2.8px;padding:1px 2px;height:8px}
.fld-name{left:0;top:0;width:64px}.fld-email{left:0;top:14px;width:64px}.fld-subject{left:0;top:28px;width:64px}
.fld-msg{left:70px;top:0;width:64px;height:22px}
.send-btn{position:absolute;left:70px;top:28px;width:64px;height:8px;background:var(--orange);color:#fff;font-size:2.8px;display:flex;align-items:center;justify-content:center}

.footer{top:790px;height:45px;background:var(--charcoal);color:#ddd;font-size:2.9px}
.footer-tab{position:absolute;left:28px;top:0;width:12px;height:10px;background:var(--orange)}
.footer-links{position:absolute;left:28px;top:18px;display:grid;grid-template-columns:26px 30px;row-gap:1px}
.footer-copy{position:absolute;left:28px;top:36px}
.footer-copy span{color:var(--orange)}
.footer-social{position:absolute;left:170px;top:6px;display:flex;gap:7px}
.footer-social i{display:block;width:5px;height:5px;border-radius:50%;background:#bbb}
.footer-about{position:absolute;left:135px;top:18px;width:80px}
</style>
</head>
<body>

<div class="brand-strip"><span class="strip-light"></span><span class="strip-dark"></span><span class="strip-orange"></span></div>

<div class="badge-logo">
  <div class="badge-name">Turf Bloom</div>
  <div class="badge-url">www.turfbloom.com</div>
  <svg class="badge-shield" width="94" height="80" viewBox="0 0 94 80">
    <polygon points="0,0 94,0 94,56 47,80 0,56" fill="#3b3b3b"/>
    <rect x="40" y="24" width="14" height="14" fill="#ffffff"/>
  </svg>
</div>

<div class="wordmark">Turf Bloom</div>

<main class="hero-screen">
  <div class="hero-photo" role="img" aria-label="Photo of a hand resting on freshly cut green grass"></div>
  <nav class="hero-nav"><span>We do</span><span>We are</span><span>Service area</span><span>Pricing</span></nav>
  <svg class="hero-burger" width="28" height="16" viewBox="0 0 28 16"><path d="M0 2H28M0 14H28" stroke="#fff" stroke-width="2.5"/></svg>
  <div class="hero-logo">Turf Bloom</div>
  <div class="hero-offer">
    <div class="hero-percent">35%</div>
    <div class="hero-tagline">Discount, our special over for today.</div>
  </div>
  <a class="hero-book">Book now</a>
  <svg class="hero-chevron" width="24" height="14" viewBox="0 0 24 14"><path d="M1 1L12 12L23 1" fill="none" stroke="#fff" stroke-width="2"/></svg>
</main>

<div class="page">
  <section class="mini-hero">
    <div class="photo" role="img" aria-label="Photo of a hand on green grass"></div>
    <div class="mini-logo">Turf Bloom</div>
    <div class="mini-nav"><span>We do</span><span>We are</span><span>Service area</span><span>Pricing</span></div>
    <div class="mini-burger"></div>
    <div class="mini-offer"><b>35%</b>Discount, our special over for today.</div>
    <div class="mini-book">Book now</div>
    <svg class="mini-chevron" width="8" height="5" viewBox="0 0 8 5"><path d="M0.5 0.5L4 4L7.5 0.5" fill="none" stroke="#fff" stroke-width=".8"/></svg>
  </section>

  <section class="we-do">
    <div class="section-title">We do</div>
    <div class="section-rule"></div>
    <p class="section-text">We mow, trim and edge lawns across the Triad with same day and next day visits. Book online in minutes, see your price up front and relax while our crew keeps your grass sharp.</p>
  </section>

  <section class="service-band"></section>
  <section class="service-cards">
    <div class="card card-1"><div class="img" role="img" aria-label="Photo of a lawn sprinkler"></div><div class="caption"><strong>Watering</strong>Smart care for green, healthy lawns all season.</div></div>
    <div class="card card-2"><div class="img" role="img" aria-label="Photo of a ride-on mower on a lawn"></div><div class="caption"><strong>Mowing</strong>Clean even cuts on every visit we make.</div></div>
    <div class="card card-3"><div class="img" role="img" aria-label="Photo of fresh grass close up"></div><div class="caption"><strong>Edging</strong>Crisp borders along paths, beds and drives.</div></div>
  </section>

  <section class="zip">
    <div class="zip-label">Only 5 minutes to get your service here</div>
    <div class="zip-form"><div class="zip-input">Enter your zip code here</div><div class="zip-btn">Next</div></div>
  </section>

  <section class="why">
    <div class="section-title">Why we are</div>
    <div class="section-rule"></div>
    <p class="section-text">Five reasons Triad homeowners choose us first. Quick booking, fair prices and a crew you can trust.</p>
  </section>

  <section class="features">
    <div class="feature f1">
      <svg width="12" height="12" viewBox="0 0 12 12"><circle cx="6" cy="6" r="5" fill="none" stroke="#e8601c" stroke-width=".7"/><path d="M2.5 9.5L9.5 2.5" stroke="#e8601c" stroke-width=".7"/></svg>
      <div><strong>No contract</strong>Pay per visit, cancel any time.</div>
    </div>
    <div class="feature f2">
      <svg width="12" height="12" viewBox="0 0 12 12"><path d="M1 3L2 4L3.5 2M1 7L2 8L3.5 6M5 3H11M5 7H11M5 10.5H11" fill="none" stroke="#e8601c" stroke-width=".7"/></svg>
      <div><strong>Instant scheduling</strong>Pick a slot and book online.</div>
    </div>
    <div class="feature f3">
      <svg width="12" height="12" viewBox="0 0 12 12"><rect x="1" y="2" width="10" height="9" fill="none" stroke="#e8601c" stroke-width=".7"/><path d="M1 4.5H11M6 6V10" stroke="#e8601c" stroke-width=".7"/></svg>
      <div><strong>Same day service</strong>Order by noon, mowed by evening.</div>
    </div>
    <div class="feature f4">
      <svg width="12" height="12" viewBox="0 0 12 12"><rect x="2" y="1" width="7" height="9" fill="none" stroke="#e8601c" stroke-width=".7"/><circle cx="8.5" cy="9" r="1.8" fill="#e8601c"/></svg>
      <div><strong>Full licensed and insured</strong>Trained crews, fully covered for your peace.</div>
    </div>
    <div class="feature f5">
      <svg width="12" height="12" viewBox="0 0 12 12"><circle cx="6" cy="7" r="4" fill="none" stroke="#e8601c" stroke-width=".7"/><path d="M6 5V9M4.5 2H7.5" stroke="#e8601c" stroke-width=".7"/></svg>
      <div><strong>Money back guarantee</strong>Not happy? We refund your visit.</div>
    </div>
  </section>

  <section class="we-are">
    <div class="section-title">We are</div>
    <div class="section-rule"></div>
    <p class="section-text">Local crews from the Piedmont Triad, proud of every lawn we cut and every promise we keep.</p>
    <svg class="we-are-badge" width="14" height="14" viewBox="0 0 14 14"><polygon points="0,0 14,0 14,10 7,14 0,10" fill="#e8601c"/></svg>
  </section>

  <section class="video">
    <div class="photo" role="img" aria-label="Photo of a lawn mower on a green lawn"></div>
    <div class="section-title">Watch our video</div>
    <div class="section-rule"></div>
    <p class="section-text">See how a visit works from booking to the final clean edge.</p>
    <svg class="play" width="26" height="26" viewBox="0 0 26 26"><circle cx="13" cy="13" r="12" fill="none" stroke="#fff" stroke-width="1.4"/><polygon points="10,7.5 19,13 10,18.5" fill="#fff"/></svg>
  </section>

  <section class="contact">
    <div class="section-title">Contact us</div>
    <div class="section-rule"></div>
    <div class="contact-form">
      <div class="field fld-name">Name</div>
      <div class="field fld-email">E-mail</div>
      <div class="field fld-subject">Subject</div>
      <div class="field fld-msg">Message</div>
      <div class="send-btn">Send</div>
    </div>
  </section>

  <footer class="footer page-footer" style="position:absolute;left:0;top:790px;width:100%;height:45px;background:var(--charcoal);color:#ddd;font-size:2.9px">
    <div class="footer-tab"></div>
    <div class="footer-links"><span>We do</span><span>Pricing</span><span>We are</span><span>FAQ</span><span>Service area</span><span>Contact us</span></div>
    <div class="footer-copy">© 2015 <span>turfbloom.com</span> all rights reserved.</div>
    <div class="footer-social"><i></i><i></i><i></i></div>
    <div class="footer-about">Turf Bloom, same day lawn care for the Piedmont Triad. Call us or book online any day.</div>
  </footer>
</div>

</body>
</html>
```